Business Card Design Project

We have 2 businesses which help each other.

Maplewick Care (providing nurses to hospitals/nursing homes etc)

and

Maplewick HR (providing nurses to our maplewick care business - but also providing workers for farms, restaurants meatworks etc)

We would like 2 separate business cards - but similar design and feel

Target Market(s)

Managers of nursing homes, hospitals, farms, meatworks, restauants

Industry/Entity Type

Business

Requirements
Must have
• both logos
https://www.filecrate.example/s/9q2m7t4kzrx8vbn/MaplewickHR-Logo-Horizontal.ai
https://www.filecrate.example/s/kp57wx2nb8y4q1h/73918_215607_88264_sourcefile.ai

You may edit the layout of Maplewick HR logo

Name
position
mobile
Phone
name@maplewickhr.com.au
mapelwickhr.com.au

Name
position
mobile
phone
name@maplewickcare.net.au
maplewickcare.net.au

```html
<!DOCTYPE html>
<html lang="en">
<head>
<meta charset="utf-8">
<title>MaplewickHR Business Card</title>
<link rel="stylesheet" href="https://fonts.googleapis.com/css2?family=Montserrat:wght@400;500;700;800&display=swap">
<style>
  :root {
    --page-bg: #e9edf0;
    --card-front: #4cb1e6;
    --card-back: #ffffff;
    --brand-blue: #0d58a6;
    --brand-mid: #2f86cf;
    --text-dark: #2b2f33;
    --map-light: #dcecf8;
    --map-soft: #eaf3fb;
    --mark-grey: #d4d8dc;
    --shadow: rgba(20, 40, 60, 0.18);
  }
  * { box-sizing: border-box; margin: 0; padding: 0; }
  html, body {
    width: 1200px;
    height: 960px;
    overflow: hidden;
    background: var(--page-bg);
    font-family: "Montserrat", sans-serif;
  }
  .sheet {
    position: relative;
    width: 1200px;
    height: 960px;
  }
  .card {
    position: absolute;
    left: 240px;
    width: 720px;
    height: 400px;
    box-shadow: 0 10px 30px var(--shadow);
    overflow: hidden;
  }
  .card--front { top: 60px; background: var(--card-front); }
  .card--back  { top: 500px; background: var(--card-back); }

  .brand {
    display: flex;
    align-items: center;
  }
  .brand__dot {
    border-radius: 50%;
    background: var(--mark-grey);
    flex: none;
  }
  .brand__name {
    font-weight: 800;
    color: var(--brand-blue);
    letter-spacing: -0.02em;
    line-height: 1;
  }

  .card--front .brand {
    position: absolute;
    left: 0; right: 0; top: 0; bottom: 0;
    justify-content: center;
    gap: 22px;
  }
  .card--front .brand__dot { width: 120px; height: 120px; }
  .card--front .brand__name { font-size: 66px; }

  .card--back .brand {
    position: absolute;
    left: 40px;
    top: 36px;
    gap: 12px;
  }
  .card--back .brand__dot { width: 54px; height: 54px; }
  .card--back .brand__name { font-size: 34px; color: var(--brand-mid); }

  .person {
    position: absolute;
    left: 52px;
    top: 128px;
  }
  .person__name {
    font-weight: 700;
    font-size: 26px;
    color: var(--brand-blue);
  }
  .person__role {
    font-weight: 500;
    font-size: 24px;
    color: var(--text-dark);
    margin-top: 2px;
  }

  .contacts {
    position: absolute;
    left: 52px;
    top: 226px;
    list-style: none;
  }
  .contacts__item {
    display: flex;
    align-items: center;
    gap: 14px;
    font-size: 19px;
    font-weight: 500;
    color: var(--text-dark);
    height: 36px;
  }
  .contacts__icon { width: 16px; height: 16px; flex: none; }

  .map-area {
    position: absolute;
    right: 0;
    top: 20px;
    width: 330px;
    height: 370px;
    background: radial-gradient(ellipse at 60% 60%, var(--map-light) 0%, var(--map-soft) 60%, var(--card-back) 100%);
  }
</style>
</head>
<body>
<main class="sheet">

  <section class="card card--front" aria-label="Card front">
    <div class="brand">
      <span class="brand__dot"></span>
      <span class="brand__name">maplewickHR</span>
    </div>
  </section>

  <section class="card card--back" aria-label="Card back">
    <div class="map-area" role="img" aria-label="Faint light-blue map of Taiwan and Australia with staff location markers"></div>

    <div class="brand">
      <span class="brand__dot"></span>
      <span class="brand__name">maplewickHR</span>
    </div>

    <div class="person">
      <p class="person__name">Daniel Reeve</p>
      <p class="person__role">Director</p>
    </div>

    <ul class="contacts">
      <li class="contacts__item">
        <svg class="contacts__icon" viewBox="0 0 16 16" aria-hidden="true">
          <path d="M3 1.5l3 .5 1 3-2 1.5c.8 1.8 2.2 3.2 4 4l1.5-2 3 1 .5 3-2 1.5C7 14 2 9 1.5 3.5z" fill="#2f86cf"/>
        </svg>
        + 61 400 555 218
      </li>
      <li class="contacts__item">
        <svg class="contacts__icon" viewBox="0 0 16 16" aria-hidden="true">
          <rect x="4" y="1" width="8" height="14" rx="1.5" fill="#2f86cf"/>
          <rect x="5.5" y="3" width="5" height="8" fill="#fff"/>
        </svg>
        + 61 (0)2 5550 1472
      </li>
      <li class="contacts__item">
        <svg class="contacts__icon" viewBox="0 0 16 16" aria-hidden="true">
          <rect x="1" y="3" width="14" height="10" rx="1" fill="#0d58a6"/>
          <path d="M1.5 3.5L8 9l6.5-5.5" stroke="#fff" stroke-width="1.3" fill="none"/>
        </svg>
        name@maplewickhr.com.au
      </li>
      <li class="contacts__item">
        <svg class="contacts__icon" viewBox="0 0 16 16" aria-hidden="true">
          <circle cx="8" cy="8" r="7" fill="#0d58a6"/>
          <path d="M1 8h14M8 1c-3 3.5-3 10.5 0 14M8 1c3 3.5 3 10.5 0 14" stroke="#fff" stroke-width="0.9" fill="none"/>
        </svg>
        www.mapelwickhr.com.au
      </li>
    </ul>
  </section>

</main>
</body>
</html>
```